Business Card Design

I would like a new business card for my business Drive Keystone, we operate within the automotive industry and offer customer retention solutions for independent mechanical workshops across Australia and New Zealand. The program incorporates service reminders and roadside assistance for consumers and is designed to get the client back for their vehicle service visit, I would like a doubled sided design that incorporates my logos and a two tone type card that has white and a carbon fibre look also use the blue in the logo I have uploaded. It would be great to have icons as the phone/fax/email etc details for the card are below. The finished design must be a print ready file useable.It would be great if the design could communicate the what type of business we are
Philip Marsh
General Manager
Drive Keystone Pty Ltd
Unit 5/42 Tolmer Street
Kelverton Brayside WST 4127
Ph:+61247318500
fax:+61247318600
Mobile:0412958364
Email:info@drivekeystone.com.au
Updates
I have just upload a carbon fibre background for the business card hope it helps
Hello guys I am sorry fr no feedback I have been away over seas I will send feedback when I return monday
Industry/Entity Type
Automotive
Look and feel
Each slider illustrates characteristics of the customer's brand and the style your logo design should communicate.

```html
<!DOCTYPE html>
<html lang="en">
<head>
<meta charset="utf-8">
<title>Drive Keystone – Business Card</title>
<link rel="stylesheet" href="https://fonts.googleapis.com/css2?family=Barlow:wght@400;700&display=swap">
<style>
  :root {
    --page: #ececec;
    --carbon-dark: #141414;
    --carbon-mid: #2b2b2b;
    --brand-blue: #2ea3dc;
    --ink-light: #f2f2f2;
    --ink-soft: #d6d6d6;
  }
  * { box-sizing: border-box; margin: 0; padding: 0; }
  html, body {
    width: 1200px; height: 1200px; overflow: hidden;
    background: var(--page);
    font-family: "Barlow", Arial, sans-serif;
  }
  .sheet {
    width: 1200px; height: 1200px;
    display: flex; flex-direction: column; align-items: center; justify-content: center;
    gap: 60px;
  }
  .card {
    position: relative;
    width: 900px; height: 514px;
    border-radius: 6px;
    overflow: hidden;
    box-shadow: 0 10px 28px rgba(0,0,0,.22);
    color: var(--ink-light);
  }
  .carbon-texture {
    position: absolute; inset: 0;
    background: radial-gradient(ellipse at 55% 35%, var(--carbon-mid) 0%, var(--carbon-dark) 75%);
  }
  /* Front */
  .card-front .brand-mark {
    position: absolute; left: 70px; top: 48px;
    display: flex; align-items: center; gap: 16px;
  }
  .brand-dot {
    width: 58px; height: 58px; border-radius: 50%;
    background: var(--brand-blue);
  }
  .brand-name {
    font-weight: 700; font-size: 26px; letter-spacing: 2px;
    text-transform: uppercase; color: var(--brand-blue);
  }
  .person {
    position: absolute; left: 70px; top: 150px;
  }
  .person-name {
    font-weight: 700; font-size: 38px; letter-spacing: 1px;
    color: var(--brand-blue); text-transform: uppercase; line-height: 1;
  }
  .person-role {
    font-size: 22px; letter-spacing: 1.5px; text-transform: uppercase;
    color: var(--ink-light); margin-top: 6px;
  }
  .address {
    position: absolute; left: 70px; top: 250px;
    font-style: normal;
    font-size: 20px; line-height: 1.45; letter-spacing: .8px; color: var(--ink-soft);
  }
  .divider {
    position: absolute; left: 380px; top: 250px;
    width: 1px; height: 160px; background: var(--ink-soft);
  }
  .contacts {
    position: absolute; left: 410px; top: 300px;
    display: grid; grid-template-columns: 90px auto; row-gap: 4px;
    font-size: 20px; letter-spacing: .8px; color: var(--ink-soft);
  }
  .contacts dd::before { content: ": "; }
  /* Back */
  .card-back .brand-lockup {
    position: absolute; inset: 0;
    display: flex; align-items: center; justify-content: center; gap: 28px;
  }
  .card-back .brand-dot { width: 120px; height: 120px; }
  .card-back .brand-name { font-size: 56px; letter-spacing: 5px; }
</style>
</head>
<body>
<main class="sheet">
  <section class="card card-front" aria-label="Business card front">
    <div class="carbon-texture" role="img" aria-label="Carbon fibre hexagon texture background"></div>
    <div class="brand-mark">
      <span class="brand-dot"></span>
      <span class="brand-name">Drive Keystone</span>
    </div>
    <div class="person">
      <h1 class="person-name">Philip Marsh</h1>
      <p class="person-role">General Manager</p>
    </div>
    <address class="address">
      Drive Keystone Pty Ltd<br>
      Unit 5/42 Tolmer Street<br>
      Kelverton Brayside<br>
      WST 4127
    </address>
    <div class="divider"></div>
    <dl class="contacts">
      <dt>Ph</dt><dd>+61247318500</dd>
      <dt>Fax</dt><dd>+61247318600</dd>
      <dt>Mobile</dt><dd>0412958364</dd>
      <dt>Email</dt><dd>info@drivekeystone.com.au</dd>
    </dl>
  </section>

  <section class="card card-back" aria-label="Business card back">
    <div class="carbon-texture" role="img" aria-label="Carbon fibre hexagon texture background"></div>
    <div class="brand-lockup">
      <span class="brand-dot"></span>
      <span class="brand-name">Drive Keystone</span>
    </div>
  </section>
</main>
</body>
</html>
```